Antique Booth hang tag design

We have just taken a booth in an Antique Mall. We have found that our off the shelf white hang tags look really tacky. We would like to create a Business Card size tag with our Company Name VONK, Booth Number 27 with designated lines to write Price, Description, Inventory Number.We specialize in Glassware and Antique Tools, but include many fun finds in our space. We do not want to include our phone numbers or names at this time since we are a vendor in the anitque mall.

Industry/Entity Type

Business

Contact Information for Business Card

This is actually for a business card style hang tag for the booth.

Font styles to use
Decorative
Script

Requirements
Must have
• Catchy design

```html
<!DOCTYPE html>
<html lang="en">
<head>
<meta charset="utf-8">
<title>VONK – Booth 27 Hang Tag</title>
<link rel="stylesheet" href="https://fonts.googleapis.com/css2?family=Pinyon+Script&family=Cinzel:wght@400&display=swap">
<style>
  :root {
    --page-bg: #d9d9d9;
    --maroon: #3d1512;
    --maroon-deep: #2e0f0c;
    --gold-light: #f3dc86;
    --gold: #cfa43c;
    --gold-dark: #8a6418;
    --silver-light: #ffffff;
    --silver: #c9c9c9;
    --ink: #4a1210;
  }
  * { margin: 0; padding: 0; box-sizing: border-box; }
  html, body {
    width: 900px; height: 1200px; overflow: hidden;
    background: var(--page-bg);
  }
  .tag {
    position: absolute; left: 140px; top: 70px;
    width: 622px; height: 1065px;
    background: radial-gradient(ellipse at 50% 40%, #4a1a15 0%, var(--maroon) 55%, var(--maroon-deep) 100%);
    overflow: hidden;
  }
  .booth-number {
    position: absolute; left: 0; right: 0; top: 52px;
    text-align: center;
    font-family: "Pinyon Script", cursive;
    font-size: 60px; line-height: 1;
    color: var(--silver);
    background: linear-gradient(180deg, var(--silver-light) 20%, #9e9e9e 60%, var(--silver-light) 95%);
    -webkit-background-clip: text; background-clip: text;
    -webkit-text-fill-color: transparent;
  }
  .ornament {
    position: absolute; left: 55px; width: 512px;
    border-radius: 50% 50% 50% 50% / 40% 40% 40% 40%;
    background: radial-gradient(ellipse at center, rgba(243,220,134,0.45) 0%, rgba(207,164,60,0.3) 55%, rgba(138,100,24,0) 100%);
  }
  .ornament--top { top: 158px; height: 200px; }
  .ornament--bottom { top: 545px; height: 200px; }
  .brand-name {
    position: absolute; left: 72px; top: 335px;
    width: 478px; height: 190px;
  }
  .info-band {
    position: absolute; left: 0; top: 785px;
    width: 622px; height: 230px;
    border-top: 5px solid var(--gold);
    border-bottom: 5px solid var(--gold);
    background: linear-gradient(180deg, #e4e4e4 0%, #ffffff 30%, #f2f2f2 55%, #d4d4d4 100%);
  }
  .field {
    position: absolute; left: 47px; right: 48px;
    display: flex; align-items: baseline;
    font-family: "Pinyon Script", cursive;
    font-size: 40px; line-height: 1;
    color: var(--ink);
  }
  .field__rule {
    flex: 1; margin-left: 4px;
    border-bottom: 4px dotted var(--ink);
    transform: translateY(-4px);
  }
  .field--price { top: 30px; }
  .field--description { top: 101px; }
  .field--inventory { top: 172px; }
</style>
</head>
<body>
  <main class="tag">
    <div class="booth-number">Booth Number 27</div>

    <div class="ornament ornament--top" role="img" aria-label="Gold baroque flourish ornament above the name"></div>

    <svg class="brand-name" viewBox="0 0 478 190" aria-label="VONK">
      <defs>
        <linearGradient id="gold-fill" x1="0" y1="0" x2="0" y2="1">
          <stop offset="0" stop-color="#f3dc86"/>
          <stop offset="0.5" stop-color="#cfa43c"/>
          <stop offset="1" stop-color="#a67b22"/>
        </linearGradient>
      </defs>
      <text x="239" y="165" text-anchor="middle" textLength="470" lengthAdjust="spacingAndGlyphs"
            font-family="Cinzel, serif" font-size="200" fill="url(#gold-fill)">VONK</text>
    </svg>

    <div class="ornament ornament--bottom" role="img" aria-label="Gold baroque flourish ornament below the name"></div>

    <section class="info-band">
      <div class="field field--price"><span>Price:</span><span class="field__rule"></span></div>
      <div class="field field--description"><span>Description:</span><span class="field__rule"></span></div>
      <div class="field field--inventory"><span>Inventory Number:</span><span class="field__rule"></span></div>
    </section>
  </main>
</body>
</html>
```